Thornfield Marsh, LLC Website

We are a small law firm in need of a website that contains the following:
1. Attractive main page
2. About us/attorney info for three people: Leonard Thornfield (attorney), Brent Marsh (attorney), and Melinda Carrow (legal assistant). We have bio's ready to submit.
3. Blog/video page. We'd like to post blogs and videos to help drive traffic
4. Multidistrict Litigation and Class Actions page, where we post information regarding active MDLs and Class actions that we are doing intake on.
Updates

Can you also please use the color "gold" in the design and logo? Thanks.

Industry/Entity Type

Legal

Coding

Coded - Design and coding required

Number of Pages Required

1 page

Colors
0054AA
0677BA
7BADD7
CADEEF
E8F1F8

Requirements
Must have
• 1. Attractive main page 2. About us/attorney info for three people: Leonard Thornfield (attorney), Brent Marsh (attorney), and Melinda Carrow (legal assistant). We have bio's ready to submit. 3. Blog/video page. We'd like to post blogs and videos to help drive traffic 4. Multidistrict Litigation and Class Actions page, where we post information regarding active MDLs and Class actions that we are doing intake on.

```html
<!DOCTYPE html>
<html lang="en">
<head>
<meta charset="utf-8">
<title>Thornfield Marsh, LLC</title>
<link href="https://fonts.googleapis.com/css2?family=Poppins:wght@400;500;600;700&display=swap" rel="stylesheet">
<style>
:root{
  --blue:#0054AA;--blue-mid:#0677BA;--sky:#7BADD7;--pale:#CADEEF;--mist:#E8F1F8;
  --cyan:#1AA3F0;--navy:#0B1A3E;--ink:#111;--text:#3a3a3a;--white:#fff;--footer:#1B2E8C;
}
*{margin:0;padding:0;box-sizing:border-box}
html,body{width:1200px;height:4043px;overflow:hidden}
body{font-family:'Poppins',sans-serif;color:var(--ink);background:var(--white);position:relative}
.abs{position:absolute}
p{line-height:1.7}
.btn{position:absolute;display:flex;align-items:center;justify-content:center;font-size:11px;font-weight:500;letter-spacing:.3px;text-transform:uppercase;text-decoration:none}
.btn-cyan{background:var(--cyan);color:var(--white)}
.btn-white{background:var(--white);color:var(--ink)}
.title{font-weight:500;text-transform:uppercase;font-size:36px;line-height:1.2}

/* header */
.site-header{position:absolute;top:0;left:0;width:1200px;height:49px;background:var(--white)}
.logo{position:absolute;display:flex;align-items:center;gap:6px;font-weight:600;text-transform:uppercase}
.logo .mark{width:14px;height:14px;background:var(--blue)}
.site-header .logo{left:122px;top:12px;font-size:12px;color:var(--blue)}
.nav{position:absolute;top:17px;font-size:11px;font-weight:500;text-transform:uppercase}
.nav span{position:absolute;white-space:nowrap}
.nav-cta{left:952px;top:8px;width:126px;height:32px;background:var(--blue);color:var(--white)}

/* hero */
.hero{position:absolute;top:49px;left:0;width:1200px;height:623px;background:linear-gradient(180deg,#0d1e46 0%,#14284f 55%,#1c2b3f 100%)}
.hero-person{position:absolute;left:110px;top:55px;width:420px;height:568px;background:radial-gradient(ellipse at 50% 40%,#5a4a40 0%,#3a302b 55%,rgba(20,30,60,0) 78%)}
.hero .kicker{left:561px;top:112px;font-size:10px;font-weight:600;color:var(--white)}
.hero h1{position:absolute;left:560px;top:136px;font-size:55px;line-height:1.14;font-weight:700;color:var(--white);text-transform:uppercase;width:560px}
.hero p{position:absolute;left:563px;top:330px;width:460px;font-size:13px;line-height:1.35;color:var(--white)}
.hero .btn{left:563px;top:411px;width:250px;height:31px}

/* about */
.about h2{left:122px;top:722px}
.about p{position:absolute;left:122px;width:450px;font-size:13px;line-height:22.5px;color:var(--text)}
.about .btn{left:122px;top:1004px;width:131px;height:31px}
.about-video{left:122px;top:1072px;width:446px;height:260px;background:linear-gradient(120deg,#4b6b3c 0%,#6b7280 35%,#2c3a55 70%,#9aa3ad 100%)}
.play{position:absolute;left:206px;top:93px;width:70px;height:70px;border-radius:50%;background:rgba(30,50,90,.55);display:flex;align-items:center;justify-content:center}

/* contact */
.contact{left:634px;top:734px;width:444px;height:598px;background:var(--pale);border:2px solid #2a3aa8}
.contact h2{position:absolute;left:29px;top:55px;font-size:30px;font-weight:400}
.field{position:absolute;left:29px;width:380px;height:44px;background:var(--white);font-size:9px;color:#666;padding:15px 12px}
.contact .btn{left:29px;top:502px;width:380px;height:31px}

/* attorneys */
.attorneys{left:0;top:1393px;width:1200px;height:587px;background:linear-gradient(180deg,#2a6cc0 0%,#1f60b4 50%,#1556a8 100%)}
.attorneys h2{position:absolute;top:58px;width:100%;text-align:center;color:var(--white);font-size:38px;font-weight:500}
.attorneys .lead{position:absolute;left:320px;top:109px;width:560px;text-align:center;color:var(--white);font-size:13px;line-height:19px}
.card{position:absolute;top:228px;height:296px;overflow:hidden}
.card .name-bar{position:absolute;left:0;bottom:0;width:100%;height:53px;background:rgba(20,60,130,.45);color:var(--white);font-weight:600;font-size:18px;text-transform:uppercase;display:flex;align-items:center;padding-left:22px}
.arrow{position:absolute;width:31px;height:31px;border-radius:50%;background:var(--cyan);display:flex;align-items:center;justify-content:center}
.card .arrow{right:16px;bottom:11px}

/* practice */
.practice h2{top:2030px;left:0;width:1200px;text-align:center;font-weight:500}
.area{position:absolute;top:2118px;width:224px;height:257px;background:var(--mist);border:2px solid #b3d0ea;text-align:center}
.area svg{position:absolute;left:87px;top:28px}
.area h3{position:absolute;top:103px;width:100%;font-size:14px;font-weight:500;line-height:18px;text-transform:uppercase}
.area p{position:absolute;top:160px;left:10px;width:200px;font-size:9px;line-height:11px;color:var(--text)}
.area .arrow{left:96px;top:203px;width:29px;height:29px}

/* mdl */
.mdl{left:0;top:2437px;width:1200px;height:364px;background:var(--pale)}
.mdl-photo{position:absolute;left:0;top:0;width:540px;height:364px;background:linear-gradient(90deg,#6f87a8 0%,#9fb7d3 45%,#c6d9ec 100%)}
.mdl h2{position:absolute;left:593px;top:51px;font-size:36px;font-weight:400;line-height:50px;text-transform:uppercase;width:560px}
.mdl p{position:absolute;left:593px;top:159px;width:490px;font-size:15px;line-height:22.5px;color:var(--ink)}
.mdl .btn{left:593px;top:270px;width:264px;height:32px}

/* blog */
.blog h2{left:122px;top:2853px;font-weight:500}
.view-more{position:absolute;left:934px;top:2864px;width:144px;height:28px;border:1.5px solid var(--cyan);font-size:10px;font-weight:600;display:flex;align-items:center;justify-content:center;gap:5px}
.post{position:absolute;top:2940px;height:399px;border:2px solid #9bcaf0;background:var(--white)}
.post .thumb{height:191px}
.post .date{position:absolute;left:23px;top:215px;font-size:10px;color:#555}
.post h3{position:absolute;left:23px;top:240px;width:260px;font-size:16px;line-height:21px;font-weight:600;text-transform:uppercase}
.post p{position:absolute;left:23px;width:265px;font-size:11px;line-height:19px;color:var(--text)}
.post .more{position:absolute;left:23px;font-size:10px;font-weight:500;color:var(--cyan);text-transform:uppercase}

/* get in touch */
.touch{left:0;top:3402px;width:1200px;height:270px;background:linear-gradient(90deg,#0a2f8c 0%,#1246a6 50%,#0a2f8c 100%);text-align:center;color:var(--white)}
.touch h2{position:absolute;top:60px;width:100%;font-size:37px;font-weight:500}
.touch p{position:absolute;left:340px;top:112px;width:520px;font-size:13px;line-height:24px}
.touch .btn{left:522px;top:180px;width:156px;height:30px}

/* footer */
.site-footer{left:0;top:3672px;width:1200px;height:371px;background:linear-gradient(180deg,#1a2c8a 0%,#1c30a0 100%);color:var(--white)}
.site-footer .logo{left:122px;top:64px;font-size:15px;color:var(--white)}
.site-footer .logo .mark{background:var(--white)}
.site-footer .about-text{position:absolute;left:122px;top:118px;width:300px;font-size:11px;line-height:15px}
.site-footer h4{position:absolute;top:60px;font-size:14px;font-weight:500;text-transform:uppercase}
.links{position:absolute;left:570px;top:106px;font-size:11px;line-height:27px;list-style:none}
.social{position:absolute;left:760px;width:24px;height:24px;border:1.5px solid var(--white);border-radius:50%}
.news-label{position:absolute;left:883px;top:106px;font-size:11px}
.news-input{position:absolute;left:883px;top:136px;width:113px;height:32px;border:1px solid var(--white);font-size:10px;padding:8px}
.news-btn{position:absolute;left:996px;top:136px;width:82px;height:32px;background:var(--white);color:var(--ink);font-size:12px;font-weight:500;display:flex;align-items:center;justify-content:center}
.legal{position:absolute;top:300px;font-size:9px}
</style>
</head>
<body>

<header class="site-header">
  <div class="logo"><span class="mark"></span>Thornfield Marsh, LLC</div>
  <nav class="nav">
    <span style="left:422px">Professionals</span>
    <span style="left:548px">Capabilities</span>
    <span style="left:657px">Our Insights</span>
    <span style="left:772px">Careers</span>
    <span style="left:859px">About Us</span>
  </nav>
  <a class="btn nav-cta">Contact Us</a>
</header>

<section class="hero">
  <div class="hero-person" role="img" aria-label="Portrait of a smiling attorney with arms crossed in front of a city skyline"></div>
  <div class="abs kicker">THORNFIELD MARSH LLC</div>
  <h1>Innovative legal solutions for your business.</h1>
  <p>Lorem ipsum dolor sit amet, consectetur adipiscing elit. Integer gravida metus velit, in consectetur arcu malesuada sit amet. Phasellus neque sem, sagittis quis condimentum et, egestas quis mi.</p>
  <a class="btn btn-cyan">Start with a consultation</a>
</section>

<section class="about">
  <h2 class="abs title">About Us</h2>
  <p style="top:776px">Lorem ipsum dolor sit amet, consectetur adipiscing elit. Integer gravida metus velit, in consectetur arcu malesuada sit amet. Phasellus neque sem, sagittis quis condimentum et, egestas quis mi. Vestibulum justo eros, blandit ac nulla vitae, tristique commodo elit.</p>
  <p style="top:888px">Lorem ipsum dolor sit amet, consectetur adipiscing elit. Integer gravida metus velit, in consectetur arcu malesuada sit amet. Phasellus neque sem, sagittis quis condimentum et, egest as quis mi. Vestibulum justo eros, blandit ac nulla vitae, tristique commodo elit.</p>
  <a class="btn btn-cyan">Learn More</a>
  <div class="abs about-video" role="img" aria-label="Video still of an attorney in a suit gesturing at his desk">
    <div class="play"><svg width="26" height="30" viewBox="0 0 26 30"><path d="M2 1 L25 15 L2 29 Z" fill="#fff"/></svg></div>
  </div>
</section>

<form class="abs contact">
  <h2>CONTACT US</h2>
  <div class="field" style="top:108px">Name</div>
  <div class="field" style="top:165px">Last Name</div>
  <div class="field" style="top:223px">Email</div>
  <div class="field" style="top:279px">Phone Number</div>
  <div class="field" style="top:337px;height:138px">Case details or message</div>
  <a class="btn btn-cyan">Start your case</a>
</form>

<section class="abs attorneys">
  <h2>MEET OUR ATTORNEYS</h2>
  <p class="lead">Lorem ipsum dolor sit amet, consectetur adipiscing elit. Integer gravida metus velit, in consectetur arcu malesuada sit amet. Phasellus neque sem, sagittis quis condimentum et, egestas quis mi. Vestibulum justo eros, blandit ac nulla vitae, tristique commodo elit. Quisque at faucibus metus, eu scelerisque nulla.</p>
  <div class="card" style="left:122px;width:297px;background:linear-gradient(180deg,#3c3c3c,#1e1e1e)" role="img" aria-label="Portrait of Leonard Thornfield in a dark suit">
    <div class="name-bar">Leonard Thornfield</div>
    <div class="arrow"><svg width="10" height="10" viewBox="0 0 10 10"><path d="M3 1 L7 5 L3 9" stroke="#fff" stroke-width="1.6" fill="none"/></svg></div>
  </div>
  <div class="card" style="left:447px;width:306px;background:linear-gradient(180deg,#6d645b,#2e2a27)" role="img" aria-label="Portrait of Brent Marsh holding a book">
    <div class="name-bar">Brent Marsh</div>
    <div class="arrow"><svg width="10" height="10" viewBox="0 0 10 10"><path d="M3 1 L7 5 L3 9" stroke="#fff" stroke-width="1.6" fill="none"/></svg></div>
  </div>
  <div class="card" style="left:772px;width:306px;background:linear-gradient(180deg,#d8d8d8,#3a3a3a)" role="img" aria-label="Portrait of Melinda Carrow in a black robe">
    <div class="name-bar">Melinda Carrow</div>
    <div class="arrow"><svg width="10" height="10" viewBox="0 0 10 10"><path d="M3 1 L7 5 L3 9" stroke="#fff" stroke-width="1.6" fill="none"/></svg></div>
  </div>
</section>

<section class="practice">
  <h2 class="abs title">Our Practice Areas</h2>
  <div class="area" style="left:122px">
    <svg width="50" height="40" viewBox="0 0 50 40"><rect x="2" y="18" width="22" height="12" rx="3" fill="#1a8fe0"/><rect x="26" y="18" width="22" height="12" rx="3" fill="#1a8fe0"/><circle cx="8" cy="32" r="3" fill="#0054AA"/><circle cx="19" cy="32" r="3" fill="#0054AA"/><circle cx="31" cy="32" r="3" fill="#0054AA"/><circle cx="42" cy="32" r="3" fill="#0054AA"/><path d="M25 4v8M19 7l3 5M31 7l-3 5" stroke="#e04040" stroke-width="2"/></svg>
    <h3>Car and Truck<br>Accident</h3>
    <p>Lorem ipsum dolor sit amet, consectetur adipiscing elit. Donec maximus..</p>
    <div class="arrow"><svg width="10" height="10" viewBox="0 0 10 10"><path d="M3 1 L7 5 L3 9" stroke="#fff" stroke-width="1.6" fill="none"/></svg></div>
  </div>
  <div class="area" style="left:366px">
    <svg width="50" height="40" viewBox="0 0 50 40"><rect x="10" y="16" width="34" height="14" rx="4" fill="#1a8fe0"/><circle cx="17" cy="32" r="4" fill="#0054AA"/><circle cx="37" cy="32" r="4" fill="#0054AA"/><circle cx="10" cy="10" r="7" fill="#1a8fe0"/></svg>
    <h3>Rideshare<br>Accidents</h3>
    <p>Lorem ipsum dolor sit amet, consectetur adipiscing elit. Donec maximus..</p>
    <div class="arrow"><svg width="10" height="10" viewBox="0 0 10 10"><path d="M3 1 L7 5 L3 9" stroke="#fff" stroke-width="1.6" fill="none"/></svg></div>
  </div>
  <div class="area" style="left:609px">
    <svg width="50" height="50" viewBox="0 0 50 50"><circle cx="25" cy="11" r="8" fill="#1a8fe0"/><path d="M10 46 V32 a15 12 0 0 1 30 0 V46 Z" fill="#1a8fe0"/></svg>
    <h3>Catastrophic<br>Injury</h3>
    <p>Lorem ipsum dolor sit amet, consectetur adipiscing elit. Donec maximus..</p>
    <div class="arrow"><svg width="10" height="10" viewBox="0 0 10 10"><path d="M3 1 L7 5 L3 9" stroke="#fff" stroke-width="1.6" fill="none"/></svg></div>
  </div>
  <div class="area" style="left:854px">
    <svg width="50" height="50" viewBox="0 0 50 50"><circle cx="30" cy="6" r="5" fill="#1a8fe0"/><circle cx="13" cy="40" r="7" fill="none" stroke="#1a8fe0" stroke-width="3"/><path d="M18 38 L28 24 L36 30" stroke="#1a8fe0" stroke-width="4" fill="none"/></svg>
    <h3>Motorcycle<br>Accident</h3>
    <p>Lorem ipsum dolor sit amet, consectetur adipiscing elit. Donec maximus..</p>
    <div class="arrow"><svg width="10" height="10" viewBox="0 0 10 10"><path d="M3 1 L7 5 L3 9" stroke="#fff" stroke-width="1.6" fill="none"/></svg></div>
  </div>
</section>

<section class="abs mdl">
  <div class="mdl-photo" role="img" aria-label="Smiling attorney with arms crossed in front of an office building"></div>
  <h2>Multidistrict Litigation and Class Actions Page</h2>
  <p>Lorem ipsum dolor sit amet, consectetur adipiscing elit. Donec maximus eros id purus ultricies, sit amet imperdiet nunc luctus. Praesent ultricies volutpat ex, posuere vulputate augue interdum in. Vivamus lobortis ultricies finibus.</p>
  <a class="btn btn-white">Learn More</a>
</section>

<section class="blog">
  <h2 class="abs title">Blog</h2>
  <a class="view-more">VIEW MORE NEWS <svg width="8" height="8" viewBox="0 0 10 10"><path d="M3 1 L7 5 L3 9" stroke="#111" stroke-width="1.5" fill="none"/></svg></a>
  <article class="post" style="left:122px;width:306px">
    <div class="thumb" role="img" aria-label="Highway running through green fields" style="background:linear-gradient(180deg,#b9d4ea 0%,#6f9a5a 40%,#5d6268 100%)"></div>
    <div class="date">APRIL 7, 2025</div>
    <h3>The Slippery Slope of HIPAA Noncompliance</h3>
    <p style="top:292px">Lorem ipsum dolor sit amet, consectetur adipiscing elit. Donec maximus eros id purus ultricies, sit amet imperdiet nunc luctus.</p>
    <div class="more" style="top:368px">Learn More ›</div>
  </article>
  <article class="post" style="left:446px;width:306px">
    <div class="thumb" role="img" aria-label="Woman on the phone reviewing documents at a desk" style="background:linear-gradient(120deg,#4a4038 0%,#8b8a84 50%,#d9d6cf 100%)"></div>
    <div class="date">APRIL 7, 2025</div>
    <h3>Money Talks: FDIC Issues Updated Crypto Guidance</h3>
    <p style="top:292px">Lorem ipsum dolor sit amet, consectetur adipiscing elit. Donec maximus eros id purus ultricies, sit amet imperdiet nunc luctus.</p>
    <div class="more" style="top:368px">Learn More ›</div>
  </article>
  <article class="post" style="left:771px;width:307px">
    <div class="thumb" role="img" aria-label="Man in black clothing holding an open book" style="background:linear-gradient(90deg,#e7e7e7 0%,#9a9a9a 50%,#2b2b2b 100%)"></div>
    <div class="date">APRIL 7, 2025</div>
    <h3>Significant Amendments to the Delaware General Corporation Law</h3>
    <p style="top:313px">Lorem ipsum dolor sit amet, consectetur adipiscing elit. Donec maximus eros id purus</p>
    <div class="more" style="top:364px">Learn More ›</div>
  </article>
</section>

<section class="abs touch">
  <h2>GET IN TOUCH</h2>
  <p>Lorem ipsum dolor sit amet, consectetur adipiscing elit. Donec maximus eros id purus ultricies, sit amet imperdiet nunc luctus.</p>
  <a class="btn btn-white">Get in touch ›</a>
</section>

<footer class="abs site-footer">
  <div class="logo"><span class="mark"></span>Thornfield Marsh, LLC</div>
  <p class="about-text">Lorem ipsum dolor sit amet, consectetur adipiscing elit. Donec maximus eros id purus ultricies, sit amet imperdiet nunc luctus. Praesent ultricies volutpat ex, posuere vulputate augue interdum in.</p>
  <h4 style="left:570px">Quick Links</h4>
  <ul class="links">
    <li>Professionals</li><li>Our Insights</li><li>About Us</li><li>Capabilities</li><li>Careers</li><li>Contact Us</li>
  </ul>
  <h4 style="left:731px">Follow Us</h4>
  <span class="social" style="top:110px"></span>
  <span class="social" style="top:146px"></span>
  <span class="social" style="top:182px"></span>
  <h4 style="left:883px">Newsletter Signup</h4>
  <div class="news-label">Subscribe To Our Newsletter</div>
  <div class="news-input">Email</div>
  <div class="news-btn">Subscribe</div>
  <div class="legal" style="left:122px">Copyright © 2025 Thornfield Marsh. All rights reserved.</div>
  <div class="legal" style="left:831px">Privacy Statement and Cookie Policy &nbsp;&nbsp;&nbsp; Legal Disclaimer</div>
</footer>

</body>
</html>
```